Etiketten für Imkerei mit Spezialisierung auf Bio Lagenhonig
Zielgruppe
wiesentau.at - BioImkerei Lindorf
Kleine Nebenerwerbs Imkerei mit Spezialisierung auf Bio Lagenhonig (nähere Infos sind auf der Website nachzulesen)
Als weitere Produktlinie bieten wir Honig+ / Honig mit Zutaten wie Himbeer, Erdbeer, Haselnuss, Mohn, Ingwer, Thymian, usw an.
Zielgruppe: Personen die offen für die Vielfalt der Natur sind, gesunde und natürliche Lebensmittel lieben und die bereit sind die aufwändige, großteils manuelle, Arbeit entsprechend zu entlohnen.
Gesucht:
ÄNDERUNG: Da die Anforderung für das ausgesetzte Preisgeld offensichtlich zu komplex ist, reduziere ich die Anforderung auf Etiketten für die Produktserie Honig+, Gesamtkonzepte sind nicht erforderlich werden aber gerne angenommen.
ÜRSPRÜNGLICH:
Redesign der aktuellen Honigetiketten
Basisdesign für Lagenhonig und Honig+ das entsprechende Varianten zulässt.
Aufgabenstellung
Ich wünsche mir ein modernes, edles (oder Öko look) Design mit sehr guten Wiedererkennungswert das sich von gängigen Honigetiketten deutlich abhebt.
Das wiesentau Logo soll enthalten sein kann aber bei Bedarf angepasst werden (z.B. monocrome Verison)
Für Lagenhonig werden derzeit 400g und 100g Gläser mit hohem schwarzen DrehFix Decke und,
für Honig+ 250g und 100g mit hohem silbenen DrehFix Deckel verwendet. Beispiele sind im Webshop unter https://hofkorb.at/index.php/wiesentau ersichtilich.
Für das Ablaufdatum ist evtl. ein Feld für manuelle Stempelung vorzusehen.
Bitte die Sichtfeldregelung der EU Verpackungsverordnung einhalten.
Bisherige Etiketten hatten den Anspruch das diese auf guten Laserdruckern ausdruckbar waren - das ist jetzt nicht mehr zwingend notwendig (wäre für Kleinauflagen aber trotzdem vorteilhaft)

```html
<!DOCTYPE html>
<html lang="de">
<head>
<meta charset="utf-8">
<title>wiesentau – wabe extra Etiketten</title>
<link rel="stylesheet" href="https://fonts.googleapis.com/css2?family=Advent+Pro:wght@300&family=Quicksand:wght@400;700&display=swap">
<style>
  :root {
    --page: #ffffff;
    --paper: #f8f5f2;
    --hex-paper: #faf8f5;
    --ink: #2f2a26;
    --text-soft: #8a8580;
    --text-variant: #5f5a56;
    --gold: #d8b46c;
    --rule: #d6d0ca;
    --ginger: #fbe7a4;
    --poppy: #fbe2cd;
    --cinnamon: #ccbaa4;
    --raspberry: #bfcddd;
  }
  * { box-sizing: border-box; margin: 0; padding: 0; }
  html, body {
    width: 1200px;
    height: 781px;
    overflow: hidden;
    background: var(--page);
  }
  .sheet { position: relative; width: 1200px; height: 781px; }
  .label {
    position: absolute;
    width: 502px;
    height: 343px;
    background: var(--paper);
    overflow: hidden;
  }
  .label--ginger    { left: 47px;  top: 8px;   --flavour: var(--ginger); }
  .label--poppy     { left: 615px; top: 8px;   --flavour: var(--poppy); }
  .label--cinnamon  { left: 47px;  top: 421px; --flavour: var(--cinnamon); }
  .label--raspberry { left: 618px; top: 421px; --flavour: var(--raspberry); }

  .brand {
    position: absolute;
    top: 12px;
    left: 0;
    width: 100%;
    text-align: center;
  }
  .brand__dot {
    display: block;
    width: 13px;
    height: 13px;
    margin: 0 auto 4px;
    border-radius: 50%;
    background: var(--ink);
  }
  .brand__name {
    font-family: "Quicksand", sans-serif;
    font-weight: 700;
    font-size: 20px;
    line-height: 1;
    color: var(--ink);
  }
  .brand__tagline {
    margin-top: 4px;
    font-family: "Quicksand", sans-serif;
    font-weight: 400;
    font-size: 6px;
    color: var(--ink);
  }

  .comb {
    position: absolute;
    left: 0;
    top: 89px;
    width: 100%;
    height: 249px;
    background: var(--flavour);
  }

  .badge {
    position: absolute;
    left: 137px;
    top: 129px;
    width: 206px;
    height: 190px;
  }
  .badge svg { position: absolute; inset: 0; }
  .badge__shape { fill: var(--hex-paper); }
  .badge__text {
    position: absolute;
    inset: 0;
    display: flex;
    flex-direction: column;
    align-items: center;
    text-align: center;
    padding-top: 10px;
  }
  .badge__base {
    font-family: "Quicksand", sans-serif;
    font-weight: 400;
    font-size: 25px;
    line-height: 1;
    color: var(--text-soft);
  }
  .badge__extra {
    display: flex;
    align-items: center;
    gap: 8px;
    margin-top: 4px;
    font-family: "Quicksand", sans-serif;
    font-style: italic;
    font-size: 14px;
    line-height: 1;
    color: var(--gold);
  }
  .badge__extra::before,
  .badge__extra::after {
    content: "";
    width: 40px;
    height: 1px;
    background: var(--rule);
  }
  .badge__variant {
    margin-top: 34px;
    font-family: "Advent Pro", sans-serif;
    font-weight: 300;
    font-size: 38px;
    letter-spacing: 1px;
    line-height: 1;
    color: var(--text-variant);
  }
</style>
</head>
<body>
<main class="sheet">

  <section class="label label--ginger">
    <header class="brand">
      <span class="brand__dot"></span>
      <div class="brand__name">wiesentau</div>
      <div class="brand__tagline">honig von der wiese</div>
    </header>
    <div class="comb" role="img" aria-label="Wabenmuster mit fliegenden Bienen in Ingwergelb"></div>
    <div class="badge">
      <svg viewBox="0 0 206 190" width="206" height="190" aria-hidden="true">
        <polygon class="badge__shape" points="0,95 52,0 154,0 206,95 154,190 52,190"/>
      </svg>
      <div class="badge__text">
        <span class="badge__base">wabe</span>
        <span class="badge__extra">extra</span>
        <span class="badge__variant">INGWER</span>
      </div>
    </div>
  </section>

  <section class="label label--poppy">
    <header class="brand">
      <span class="brand__dot"></span>
      <div class="brand__name">wiesentau</div>
      <div class="brand__tagline">honig von der wiese</div>
    </header>
    <div class="comb" role="img" aria-label="Wabenmuster mit fliegenden Bienen in zartem Pfirsichton"></div>
    <div class="badge">
      <svg viewBox="0 0 206 190" width="206" height="190" aria-hidden="true">
        <polygon class="badge__shape" points="0,95 52,0 154,0 206,95 154,190 52,190"/>
      </svg>
      <div class="badge__text">
        <span class="badge__base">wabe</span>
        <span class="badge__extra">extra</span>
        <span class="badge__variant">MOHN</span>
      </div>
    </div>
  </section>

  <section class="label label--cinnamon">
    <header class="brand">
      <span class="brand__dot"></span>
      <div class="brand__name">wiesentau</div>
      <div class="brand__tagline">honig von der wiese</div>
    </header>
    <div class="comb" role="img" aria-label="Wabenmuster mit fliegenden Bienen in Zimtbraun"></div>
    <div class="badge">
      <svg viewBox="0 0 206 190" width="206" height="190" aria-hidden="true">
        <polygon class="badge__shape" points="0,95 52,0 154,0 206,95 154,190 52,190"/>
      </svg>
      <div class="badge__text">
        <span class="badge__base">wabe</span>
        <span class="badge__extra">extra</span>
        <span class="badge__variant">ZIMT</span>
      </div>
    </div>
  </section>

  <section class="label label--raspberry">
    <header class="brand">
      <span class="brand__dot"></span>
      <div class="brand__name">wiesentau</div>
      <div class="brand__tagline">honig von der wiese</div>
    </header>
    <div class="comb" role="img" aria-label="Wabenmuster mit fliegenden Bienen in Graublau"></div>
    <div class="badge">
      <svg viewBox="0 0 206 190" width="206" height="190" aria-hidden="true">
        <polygon class="badge__shape" points="0,95 52,0 154,0 206,95 154,190 52,190"/>
      </svg>
      <div class="badge__text">
        <span class="badge__base">wabe</span>
        <span class="badge__extra">extra</span>
        <span class="badge__variant">HIMBEERE</span>
      </div>
    </div>
  </section>

</main>
</body>
</html>
```